Menu Board and Flyer for a Poke Restaurant

We need for our new Menu board for a Poke restaurant. There will be 2 separate boards. 1 Board for Speciality items, the second for "Build your Own". The menu boards will be installed on a wall.

The first board is going to be 36 W x 48 H inches. The second board will be 72 W x 48 H inches.

I would also like to consolidate the board into a one Page menu flyer that can be printed on an 11 inches x 14 inches Page.

The goal is to have customers focus on the ease of ordering.
We have attached a sample design idea for reference and our logo options. Including the logo is optional.

I have included some sample menus by other companies as attachment and referance.

Files need to include any special fonts used in the design.

Target Market(s)

Young Professionals who love eating healthy, trendy, delicious new food options.

Industry/Entity Type

Fast Food Restaurant

Font styles to use
Serif
Sans Serif

Requirements
Must have
• Simple
• Clean design - NOT busy
• Fun
• Easy to follow
• Highlight a step by step ordering process.
• Light background color
• Files need to include any special fonts used in the design.
Should not have
• script fonts

```html
<!DOCTYPE html>
<html lang="en">
<head>
<meta charset="utf-8">
<title>Build Your Own – Tidewater Pokehouse</title>
<link rel="stylesheet" href="https://fonts.googleapis.com/css2?family=Josefin+Sans:wght@300;400&family=Oswald:wght@300;400&family=Pathway+Gothic+One&family=Questrial&display=swap">
<style>
  :root{
    --page:#dcdcdc;
    --card:#f7f7f7;
    --ink:#111111;
    --item:#4a4a4a;
    --muted:#7a7a7a;
    --rule:#3a3a3a;
  }
  html,body{margin:0;padding:0;width:1200px;height:1000px;overflow:hidden;background:var(--page);}
  .menu-card{
    position:absolute;left:30px;top:120px;width:1020px;height:680px;
    background:var(--card);
    transform:scale(1.1176);transform-origin:0 0;
    color:var(--ink);
  }
  .title{
    position:absolute;left:104px;top:62px;margin:0;
    font:400 54px/1 "Josefin Sans",sans-serif;letter-spacing:4px;
    word-spacing:12px;white-space:nowrap;
  }
  .title-rule{position:absolute;height:1px;background:var(--rule);top:88px;}
  .brand{position:absolute;left:790px;top:40px;width:180px;text-align:center;}
  .brand-dot{width:18px;height:18px;border-radius:50%;background:var(--ink);margin:0 auto 14px;}
  .brand-name{font:300 26px/1.15 "Josefin Sans",sans-serif;letter-spacing:3px;color:var(--ink);}
  .step{position:absolute;}
  .step-head{display:flex;align-items:flex-end;gap:2px;height:60px;}
  .step-num{font:300 62px/0.8 "Oswald",sans-serif;color:var(--ink);}
  .step-label{display:flex;flex-direction:column;padding-bottom:1px;}
  .step-kicker{font:13px/1 "Pathway Gothic One",sans-serif;letter-spacing:1px;color:var(--muted);}
  .step-name{font:400 29px/1 "Josefin Sans",sans-serif;letter-spacing:1px;margin-top:3px;}
  .options{position:absolute;border-left:1px solid var(--rule);list-style:none;margin:0;padding:6px 0 0 20px;}
  .options li{font:19px/29.5px "Pathway Gothic One",sans-serif;letter-spacing:1px;color:var(--item);white-space:nowrap;}
  .options.two-col{columns:2;column-gap:0;width:240px;}
  .styles{position:absolute;left:50px;top:245px;list-style:none;margin:0;padding:0;}
  .styles li{margin-bottom:16px;}
  .styles .style-name{display:block;font:16px/1.1 "Questrial",sans-serif;color:var(--ink);}
  .styles .style-note{display:block;font:13px/1.35 "Pathway Gothic One",sans-serif;letter-spacing:1.5px;color:var(--muted);}
</style>
</head>
<body>
<main class="menu-card">
  <span class="title-rule" style="left:38px;width:62px"></span>
  <h1 class="title">BUILD YOUR OWN</h1>
  <span class="title-rule" style="left:684px;width:64px"></span>

  <div class="brand">
    <div class="brand-dot"></div>
    <div class="brand-name">Tidewater<br>Pokehouse</div>
  </div>

  <section class="step" style="left:40px;top:158px">
    <div class="step-head"><span class="step-num">1</span><span class="step-label"><span class="step-kicker">CHOOSE YOUR</span><span class="step-name">STYLE</span></span></div>
  </section>
  <ul class="styles">
    <li><span class="style-name">classic bowl</span><span class="style-note">REGULAR OR<br>LARGE</span></li>
    <li><span class="style-name">crunchy bowl</span><span class="style-note">ONE SIZE,<br>TOSTADA STYLE</span></li>
    <li style="margin-top:26px"><span class="style-name">surfer style</span><span class="style-note">POKE SERVED<br>TACO STYLE</span></li>
    <li style="margin-top:26px"><span class="style-name">just poke</span><span class="style-note">NO BASE, 1LB OF<br>YOUR FAVORITE POKE</span></li>
  </ul>

  <section class="step" style="left:195px;top:158px">
    <div class="step-head"><span class="step-num">2</span><span class="step-label"><span class="step-kicker">CHOOSE YOUR</span><span class="step-name">FISH</span></span></div>
  </section>
  <ul class="options" style="left:204px;top:240px;height:311px">
    <li>AHI</li><li>TUNA</li><li>SALMON</li><li>HAMACHI</li><li>SPICY TUNA</li><li>SHRIMP</li><li>SCALLOP</li>
  </ul>

  <section class="step" style="left:352px;top:163px">
    <div class="step-head"><span class="step-num">3</span><span class="step-label"><span class="step-kicker">CHOOSE YOUR</span><span class="step-name">TOPPINGS</span></span></div>
  </section>
  <ul class="options" style="left:361px;top:240px;height:316px;width:240px">
    <li>CRISPY ONION</li><li>GREEN ONION,</li><li>SWEET ONION,</li><li>MASAGO</li><li>CILANTRO</li><li>CUCUMBER</li><li>CORN</li><li>COCONUT FLAKES</li><li>HAWAIIAN</li><li>SEA SALT</li><li>CHILLI FLAKES</li>
  </ul>
  <ul class="options" style="left:497px;top:240px;border-left:none">
    <li>OGO</li><li>FURIKAKE</li><li>PANKO</li><li>SESAME SEED</li><li>AVOCADO</li>
  </ul>

  <section class="step" style="left:620px;top:163px">
    <div class="step-head"><span class="step-num">4</span><span class="step-label"><span class="step-kicker">CHOOSE YOUR</span><span class="step-name">SAUCE</span></span></div>
  </section>
  <ul class="options" style="left:630px;top:240px;height:316px">
    <li>SESAME SHOYU</li><li>SIRACHA AIOLI</li><li>PONZU</li><li>SWEET SHOYU</li><li>WASABI SHOYU</li><li>SWEET CHILI</li><li>CHILI UME</li><li>GINGER SCALLION</li><li>WASABI CREME</li>
  </ul>

  <section class="step" style="left:805px;top:241px">
    <div class="step-head"><span class="step-num">5</span><span class="step-label"><span class="step-kicker">CHOOSE YOUR</span><span class="step-name">BASE</span></span></div>
  </section>
  <ul class="options" style="left:817px;top:318px;height:237px">
    <li>WHITE RICE</li><li>BROWN RICE</li><li>BLACK RICE</li><li>MIXED GREENS</li>
  </ul>
</main>
</body>
</html>
```